Flyer for swimming pool service business

I am starting up a new pool cleaning business and I'm focusing on suburbs surrounding my suburb. So it will be a local service with fast, professional and friendly service.. I would like a Flyer of A5 size to drop into letterboxes local homes.

The business is called 'Gumleaf Spa Care'

The following is what I would like in the flyer

Pool service frustrating you?
Troubled by poor water condition?
Tired of doing it yourself?

Keep your swimming pool sparkling and safe all year round

- water testing
- pool chemistry
- chlorine levels
- Ph balance
- equipment maintenance
- algae prevention
- leaf and debris maintenance
- filter cleaning
- tile cleaning
- salt water systems
- local service
- chemicals supplied and delivered
All for the low price of $40 a month (plus chemicals)

Relax and let Gumleaf Spa Care take care of it for you.
for a one off service or a monthly service
no contracts

Contact details
Mitch - 0417 283 640
gumleafspacare@quollmail.net.au

Target Market(s)

the target market is a couples and familys 40-70 years old in a well off riverside suburb

Industry/Entity Type

Pool Service

Requirements
Must have
• Am looking to have a nice blue crystal clear water as part of the background either big or small.

Include my logo (provided) feel free to change the font of the Gumleaf Spas Care writing on it, if that suits your design
Should not have
• cartoonish or funny images

```html
<!DOCTYPE html>
<html lang="en">
<head>
<meta charset="UTF-8">
<title>Gumleaf Spa Care – Flyer</title>
<link href="https://fonts.googleapis.com/css2?family=Open+Sans:wght@300;400;700;800&family=Pacifico&display=swap" rel="stylesheet">
<style>
  :root {
    --water-light: #8fd3ee;
    --water-mid: #3aa6d6;
    --water-deep: #1d7fb8;
    --panel: rgba(31, 84, 178, 0.9);
    --panel-shadow: rgba(10, 40, 90, 0.35);
    --white: #ffffff;
  }
  * { margin: 0; padding: 0; box-sizing: border-box; }
  html, body { width: 849px; height: 1200px; overflow: hidden; }
  body { font-family: "Open Sans", Arial, sans-serif; color: var(--white); }

  .flyer {
    position: relative;
    width: 849px;
    height: 1200px;
    overflow: hidden;
  }
  .water-background {
    position: absolute;
    inset: 0;
    background:
      radial-gradient(ellipse at 85% 20%, rgba(255,255,255,0.35), transparent 45%),
      radial-gradient(ellipse at 10% 80%, rgba(255,255,255,0.25), transparent 40%),
      linear-gradient(160deg, var(--water-light) 0%, var(--water-mid) 45%, var(--water-deep) 100%);
  }
  .offer-panel {
    position: absolute;
    left: 53px;
    top: 62px;
    width: 742px;
    height: 978px;
    border-radius: 22px;
    background: var(--panel);
    box-shadow: 0 6px 14px var(--panel-shadow);
  }

  .brand-mark {
    position: absolute;
    left: 105px;
    top: 128px;
    width: 250px;
    height: 152px;
    display: flex;
    align-items: center;
    gap: 12px;
  }
  .brand-mark__dot {
    flex: none;
    width: 56px;
    height: 56px;
    border-radius: 50%;
    background: var(--white);
  }
  .brand-mark__name {
    font-weight: 700;
    font-size: 24px;
    line-height: 1.15;
  }

  .business-name {
    position: absolute;
    left: 388px;
    top: 160px;
    font-family: "Pacifico", cursive;
    font-size: 31px;
    line-height: 1.2;
    white-space: nowrap;
  }

  .service-list {
    position: absolute;
    left: 100px;
    top: 314px;
    list-style: none;
    font-size: 23px;
    line-height: 30.2px;
  }
  .service-list li::before { content: "- "; }

  .divider {
    position: absolute;
    left: 100px;
    top: 692px;
    width: 645px;
    height: 2px;
    background: var(--white);
    opacity: 0.85;
  }

  .price-lead {
    position: absolute;
    left: 90px;
    top: 722px;
    font-weight: 800;
    font-size: 54px;
    line-height: 1;
    letter-spacing: 0.5px;
  }
  .price-sub {
    position: absolute;
    left: 90px;
    top: 790px;
    font-weight: 400;
    font-size: 35px;
    line-height: 1;
  }
  .price-currency {
    position: absolute;
    left: 312px;
    top: 845px;
    font-weight: 300;
    font-size: 110px;
    line-height: 1;
  }
  .price-amount {
    position: absolute;
    left: 388px;
    top: 672px;
    font-weight: 800;
    font-size: 340px;
    line-height: 1;
    letter-spacing: -10px;
  }
  .price-period {
    position: absolute;
    left: 313px;
    top: 985px;
    font-size: 38px;
    line-height: 1;
    white-space: nowrap;
  }
  .price-period strong { font-weight: 800; }
  .price-period span { font-weight: 400; font-size: 34px; }

  .contact {
    position: absolute;
    left: 70px;
    top: 1060px;
    font-size: 20px;
    line-height: 26px;
  }
  .contact h2 { font-size: 22px; font-weight: 700; line-height: 28px; }

  .terms {
    position: absolute;
    left: 460px;
    top: 1064px;
    width: 330px;
    font-size: 19px;
    line-height: 24px;
  }
</style>
</head>
<body>
<main class="flyer">
  <div class="water-background" role="img" aria-label="Crystal clear blue swimming pool water with light ripples"></div>
  <section class="offer-panel"></section>

  <div class="brand-mark">
    <span class="brand-mark__dot"></span>
    <span class="brand-mark__name">Gumleaf Spa Care</span>
  </div>
  <h1 class="business-name">Gumleaf Spa Care</h1>

  <ul class="service-list">
    <li>water testing</li>
    <li>pool chemistry</li>
    <li>chlorine levels</li>
    <li>Ph balance</li>
    <li>equipment maintenance</li>
    <li>algae prevention</li>
    <li>leaf and debris maintenance</li>
    <li>filter cleaning</li>
    <li>tile cleaning</li>
    <li>salt water systems</li>
    <li>local service</li>
    <li>chemicals supplied and delivered</li>
  </ul>

  <div class="divider"></div>

  <p class="price-lead">ALL FOR</p>
  <p class="price-sub">THE LOW PRICE OF</p>
  <p class="price-currency">$</p>
  <p class="price-amount">40</p>
  <p class="price-period"><strong>A MONTH</strong> <span>(plus chemicals)</span></p>

  <address class="contact" style="font-style: normal;">
    <h2>Contact details</h2>
    Mitch - 0417 283 640<br>
    gumleafspacare@quollmail.net.au
  </address>

  <p class="terms">For a one off service or a monthly service no contracts.</p>
</main>
</body>
</html>
```